Quorvane Capital Modern Business Card

We need a modern business card template designed for Quorvane Capital.
Quorvane Capital is a diversified global cryptocurrency investment fund.

The font under the logo: Diversified Crypto Funds

Color Hexcode: Main colors white (ffffff) & teal (188383), we are open to adding #fcca46 as an accent

Target Market(s)

Accredited Investors, high net worth individuals and institutional investors

Industry/Entity Type

Investment

Contact Information for Business Card

Contact Information should contain
Name
main phone +1 720 555 0147
cell
email

Font styles to use
Sans Serif
Other font styles liked:
• Diversified Crypto Funds

Requirements
Must have
• would like to have icons that identify the contact information
• include our website: www.quorvanecapital.example
• include our Tagline: Diversified Crypto Investment Funds
Nice to have
• Would like to have a simple back side with the logo (without the words) and plenty of space

```html
<!DOCTYPE html>
<html lang="en">
<head>
<meta charset="utf-8">
<title>Quorvane Capital Business Card</title>
<link rel="stylesheet" href="https://fonts.googleapis.com/css2?family=Noto+Sans+JP:wght@300;400&family=Open+Sans:wght@400;600&display=swap">
<style>
  :root {
    --stage: #e9e9e7;
    --card-white: #ffffff;
    --accent-yellow: #fcc846;
    --brand-teal: #1f9891;
    --ink: #1c1c1c;
    --ink-soft: #4a4a3a;
  }
  * { box-sizing: border-box; margin: 0; padding: 0; }
  html, body { width: 1200px; height: 873px; overflow: hidden; }
  body {
    background: var(--stage);
    display: flex;
    align-items: center;
    justify-content: center;
    gap: 48px;
    font-family: "Open Sans", sans-serif;
  }
  .card {
    position: relative;
    width: 520px;
    height: 300px;
    box-shadow: 0 6px 18px rgba(0,0,0,0.12);
  }
  .card--front { background: var(--accent-yellow); }
  .card--back { background: var(--card-white); display: flex; align-items: center; justify-content: center; }

  .brand {
    display: flex;
    align-items: center;
    gap: 8px;
    font-family: "Noto Sans JP", sans-serif;
    font-weight: 400;
    color: var(--brand-teal);
    letter-spacing: 0.04em;
    text-transform: uppercase;
  }
  .brand__dot { border-radius: 50%; background: var(--brand-teal); flex: none; }

  .front__brand { position: absolute; left: 34px; top: 30px; }
  .front__brand .brand { font-size: 13px; }
  .front__brand .brand__dot { width: 12px; height: 12px; }
  .brand__tagline {
    margin: 5px 0 0 20px;
    font-family: "Noto Sans JP", sans-serif;
    font-weight: 300;
    font-size: 9px;
    color: var(--ink-soft);
    letter-spacing: 0.05em;
  }

  .person { position: absolute; right: 36px; top: 112px; text-align: right; }
  .person__name {
    font-family: "Open Sans", sans-serif;
    font-weight: 400;
    font-size: 34px;
    line-height: 1;
    color: var(--brand-teal);
  }
  .person__role { margin-top: 4px; font-size: 15px; color: var(--ink); }

  .contacts {
    position: absolute;
    left: 34px;
    bottom: 28px;
    list-style: none;
    font-size: 15px;
    line-height: 1.45;
    color: var(--ink);
  }
  .contacts__item { display: flex; align-items: center; gap: 8px; }
  .contacts__icon { width: 12px; height: 12px; flex: none; fill: none; stroke: var(--brand-teal); stroke-width: 1.6; }
  .contacts__icon--solid { fill: var(--brand-teal); stroke: none; }

  .back__brand .brand { font-size: 30px; gap: 14px; color: var(--brand-teal); }
  .back__brand .brand__dot { width: 26px; height: 26px; }
</style>
</head>
<body>
  <section class="card card--front" aria-label="Business card front">
    <div class="front__brand">
      <div class="brand"><span class="brand__dot"></span>Quorvane Capital</div>
      <p class="brand__tagline">Diversified Crypto Funds</p>
    </div>

    <div class="person">
      <p class="person__name">Elsa Marlow</p>
      <p class="person__role">Director</p>
    </div>

    <ul class="contacts">
      <li class="contacts__item">
        <svg class="contacts__icon contacts__icon--solid" viewBox="0 0 12 12" aria-hidden="true"><path d="M6 0.5a4 4 0 0 1 4 4c0 3-4 7-4 7s-4-4-4-7a4 4 0 0 1 4-4z"/><circle cx="6" cy="4.5" r="1.5" fill="#fcc846"/></svg>
        Halden Company 48 W Birch Ave
      </li>
      <li class="contacts__item">
        <svg class="contacts__icon" viewBox="0 0 12 12" aria-hidden="true"><rect x="3" y="1" width="6" height="10" rx="1"/></svg>
        +1 720 555 0147
      </li>
      <li class="contacts__item">
        <svg class="contacts__icon" viewBox="0 0 12 12" aria-hidden="true"><rect x="1" y="2.5" width="10" height="7"/><path d="M1 2.5l5 4 5-4"/></svg>
        info@quorvanecapital.example
      </li>
      <li class="contacts__item">
        <svg class="contacts__icon" viewBox="0 0 12 12" aria-hidden="true"><circle cx="6" cy="6" r="5"/><path d="M1 6h10M6 1c-2.5 3-2.5 7 0 10M6 1c2.5 3 2.5 7 0 10"/></svg>
        www.quorvanecapital.example
      </li>
    </ul>
  </section>

  <section class="card card--back" aria-label="Business card back">
    <div class="back__brand">
      <div class="brand"><span class="brand__dot"></span>Quorvane Capital</div>
    </div>
  </section>
</body>
</html>
```